Web Design Project

I need designs (PSD only - no programming) for several pages of a new website helping train operators to manage key information about their traindrivers.
The main feature of this website is the management of personnel records (create, edit, search, delete). Another key aspect is the management of user privileges. Since this is a new website we also need a user friendly frontpage, pricing information and how it works sections.
This can be broken down into 9 pages for which we need designs (PSDs).
1. Home
2. Driver record
3. How it works
4. Pricing
5. User administration
6. Help
7. Record list view
8. Login
9. Registration
Navigation (not logged in) are: Home | How it works | Pricing | Customers | About us | Contact
Navigation (logged in) are: Overview | Administration | Manage records | Billing | Help | Contact
Footer: Customer logos | Awards | Terms & Conditions | Privacy
To provide the best support for you to come up with a strong design proposal I will provide DAILY feedback to all participants. We have also created concept mockups (attached) and example pages (below) for each section to give you a clear sense of what we look for.
The core concepts for a successful bid are that the website is EASY to understand, INTUITIVE to navigate, and SIMPLE to use. Most of our users lack technical background and are looking for tool to simplify their work.
The strongest participants (winner and close contenders) will have the opportunity to additional commissioned work on additional sections not included in this brief.
Example Pages (by section)
1. http://www.brovendale.example/site-keepers/
1. http://www.qvt.example/
1. http://www.mondaph.example/
1. http://www.gorvanquest.example/
2. http://www.snapveld.example/profile_edit.gne
3. https://www.tarn.example/how-it-works/
3. http://www.bulkvue.example/learn
4. http://www.pactheron.example/crm/editions-pricing.jsp
4. http://www.brovendale.example/site-keepers/prices
6. https://support.talvora.example/en-gb/
6. http://help.dealmeadow.example/contact_us
8. https://www.careweave.example/uas/login
8. https://www.dealmeadow.example/login
8. http://www.askhollow.example/login/index
For form designs we like Verindo, Bidnook, Snapveld, CareWeave, Chatterly and the concepts presented by Tomas Kerrigan in his classic Layout Craft Shaping the Input Boxes.
For additional guidance see mockups attached!
Target Market(s)
Security, human resources and admin support employees for train operators.
Industry/Entity Type
Learn
Requirements
Should not have
- Home page should not have
Social media icons (chatterly, chirpla, CareWeave, RSS feed)
Contact forms
Read more links
Old trains

```html
<!DOCTYPE html>
<html lang="en">
<head>
<meta charset="utf-8">
<title>RailLedger – Driver Record</title>
<link href="https://fonts.googleapis.com/css2?family=Arimo:wght@400;700&display=swap" rel="stylesheet">
<style>
:root{
  --blue:#1b78d2;
  --blue-dark:#0e6fb3;
  --green:#7cc41f;
  --green-dark:#62a812;
  --text:#333;
  --muted:#555;
  --line:#c9c9c9;
  --panel-bg:#fff;
  --page-bg:#f4f4f4;
  --box-bg:#f2f2f2;
  --footer-bg:#cfcfcf;
}
*{box-sizing:border-box;margin:0;padding:0}
html,body{width:1152px;height:1200px;overflow:hidden;background:var(--page-bg)}
body{font-family:"Arimo",Arial,sans-serif;color:var(--text)}
.page{position:relative;width:1200px;height:1250px;transform:scale(.96);transform-origin:0 0}
.page *{position:absolute}
.page .inline{position:static}

.header{left:0;top:0;width:1200px;height:108px;background:linear-gradient(#fff,#e4e4e4);border-top:3px solid var(--blue)}
.user-pill{left:763px;top:0;width:155px;height:27px;background:var(--blue);color:#fff;font-size:12px;border-radius:0 0 14px 14px;text-align:center;line-height:28px}
.lang-label{left:933px;top:11px;font-size:12px;color:#555}
.brand{left:119px;top:36px;font-size:36px;font-weight:700;color:var(--blue)}
.nav a{position:absolute;top:50px;font-size:17px;font-weight:700;color:var(--text);text-decoration:none;white-space:nowrap}
.nav a.active{top:45px;left:674px;width:153px;height:30px;border-radius:15px;background:var(--blue);color:#fff;text-align:center;line-height:30px}

.banner{left:0;top:108px;width:1200px;height:117px;background:radial-gradient(circle at 720px 40px,#1c8fd0 0,#0f7fbf 60%,#0c74b2 100%)}
.banner h1{left:120px;top:45px;font-size:36px;font-weight:700;color:#fff}
.tab{top:45px;width:154px;height:41px;border-radius:3px;font-size:20px;text-align:center;line-height:41px}
.tab.form{left:739px;background:linear-gradient(var(--green),var(--green-dark));color:#fff;font-weight:700}
.tab.list{left:926px;background:#fff;color:#333;box-shadow:0 2px 0 #bbb}

.tool{top:250px;width:70px;text-align:center;font-size:14px;color:#333}
.tool svg{position:static;display:block;margin:0 auto 4px}
.tool.current span{text-decoration:underline}

.panel{left:90px;top:322px;width:1024px;height:815px;background:var(--panel-bg);border:1px solid var(--line);border-radius:6px;overflow:hidden}
.panel-head{left:90px;top:322px;width:1024px;height:39px;background:linear-gradient(#84cc27,#66a814);border-radius:6px 6px 0 0;color:#fff;font-size:18px;padding:10px 22px}
.group{background:var(--box-bg);border:1px solid var(--line)}
.group-title{font-size:14px;color:#333}
.section-bar{left:91px;top:751px;width:1022px;height:31px;background:#f0f0f0;border-top:1px solid #ddd;border-bottom:1px solid #ddd}
.section-title{top:757px;font-size:18px;color:#333}
.divider{left:537px;top:751px;width:1px;height:385px;background:#ddd}

.lbl{left:0;font-size:14px;color:var(--text);text-align:right;white-space:nowrap}
.field{height:19px;border:1px solid var(--line);background:#fff;font-size:12px;color:var(--muted);padding-left:4px;line-height:17px;white-space:nowrap;overflow:hidden}
.field.focus{border-color:#9ccd4a}
.area{height:33px;line-height:13px;padding-top:2px}
.select::after{content:"";position:absolute;right:2px;top:2px;width:13px;height:13px;background:linear-gradient(#dbe8f7,#a9c4e6);border-radius:2px}
.select::before{content:"";position:absolute;right:5px;top:6px;border-left:4px solid transparent;border-right:4px solid transparent;border-top:5px solid #2e5e9e;z-index:1}
.btn{height:20px;border:1px solid #bbb;border-radius:3px;background:linear-gradient(#fafafa,#ddd);font-size:12px;color:#555;text-align:center;line-height:18px}
.hint{width:15px;height:15px;border:1px solid #bbb;border-radius:50%;font-size:10px;color:#aaa;text-align:center;line-height:13px}
.avatar{left:340px;top:587px;width:53px;height:54px;border:1px solid #ccc;border-radius:3px;background:radial-gradient(circle at 50% 45%,#f2a93b 0,#e4912a 30%,#2c5aa0 31%,#1f4a8e 70%,#fff 71%)}

.footer{left:0;top:1208px;width:1200px;height:42px;background:var(--footer-bg);font-size:12px;color:#222}
.footer .left{left:90px;top:15px}
.footer .right{right:87px;top:15px}
</style>
</head>
<body>
<div class="page">

  <header class="header">
    <div class="user-pill">Usernamehere &nbsp;|&nbsp; Logout</div>
    <div class="lang-label">Language</div>
    <div class="field select" style="left:1000px;top:8px;width:80px">English</div>
    <div class="brand">RailLedger</div>
    <nav class="nav">
      <a style="left:424px">Overview</a>
      <a style="left:534px">Administration</a>
      <a class="active">Manage Records</a>
      <a style="left:851px">Billing</a>
      <a style="left:935px">Help</a>
      <a style="left:1006px">Contact</a>
    </nav>
  </header>

  <section class="banner">
    <h1>Driver Record</h1>
    <div class="tab form">Form</div>
    <div class="tab list">List View</div>
  </section>

  <div class="tool" style="left:691px"><svg width="30" height="32" viewBox="0 0 30 32"><path d="M6 2h13l6 6v22H6z" fill="#f4f4f4" stroke="#bbb"/><circle cx="10" cy="20" r="6" fill="#999"/><path d="M10 16v8M6 20h8" stroke="#fff" stroke-width="2"/></svg><span>New</span></div>
  <div class="tool current" style="left:760px"><svg width="30" height="32" viewBox="0 0 30 32"><rect x="2" y="3" width="26" height="26" rx="2" fill="#2c7fc4"/><rect x="7" y="3" width="16" height="9" fill="#fff"/><rect x="6" y="17" width="18" height="12" fill="#7cc41f"/></svg><span>Save</span></div>
  <div class="tool" style="left:836px"><svg width="32" height="32" viewBox="0 0 32 32"><path d="M6 2h13l6 6v22H6z" fill="#f4f4f4" stroke="#777" stroke-width="1.5"/><path d="M18 19l10 10M28 19l-10 10" stroke="#555" stroke-width="3"/></svg><span>Delete</span></div>
  <div class="tool" style="left:911px"><svg width="32" height="32" viewBox="0 0 32 32"><rect x="9" y="4" width="14" height="8" fill="#fff" stroke="#999"/><rect x="3" y="11" width="26" height="12" rx="2" fill="#777"/><rect x="8" y="19" width="16" height="9" fill="#fff" stroke="#999"/></svg><span>Print</span></div>
  <div class="tool" style="left:979px"><svg width="30" height="32" viewBox="0 0 30 32"><path d="M6 2h13l6 6v22H6z" fill="#f4f4f4" stroke="#aaa"/><rect x="3" y="3" width="12" height="6" fill="#888"/><path d="M9 26c4-8 8-14 6-16s-4 6 8 12" fill="none" stroke="#c33" stroke-width="1.5"/></svg><span>PDF</span></div>
  <div class="tool" style="left:1054px"><svg width="30" height="32" viewBox="0 0 30 32"><path d="M8 2h13l6 6v22H8z" fill="#f4f4f4" stroke="#999"/><path d="M3 14h9v-4l8 8-8 8v-4H3z" fill="#666"/></svg><span>Export</span></div>

  <div class="panel"></div>
  <div class="panel-head">Personal Information</div>

  <div class="group" style="left:113px;top:379px;width:296px;height:65px"></div>
  <div class="group-title" style="left:123px;top:387px">Employer &amp; Contact</div>
  <div class="field select" style="left:123px;top:414px;width:124px">Company</div>
  <div class="field select" style="left:267px;top:414px;width:124px">Contact</div>

  <!-- personal: left column -->
  <div class="lbl" style="top:470px;width:212px">Name</div>
  <div class="field focus" style="left:224px;top:469px;width:169px">John</div>
  <div class="hint" style="left:398px;top:471px">?</div>
  <div class="lbl" style="top:500px;width:212px">Surname</div>
  <div class="field" style="left:224px;top:499px;width:169px">Doe</div>
  <div class="hint" style="left:398px;top:501px">?</div>
  <div class="lbl" style="top:530px;width:212px">Date of Birth</div>
  <div class="field select" style="left:224px;top:529px;width:63px">1977</div>
  <div class="field select" style="left:293px;top:529px;width:52px">Nov</div>
  <div class="field select" style="left:351px;top:529px;width:42px">24</div>
  <div class="hint" style="left:398px;top:531px">?</div>
  <div class="lbl" style="top:560px;width:212px">Place of Birth</div>
  <div class="field" style="left:224px;top:559px;width:169px">Doe</div>
  <div class="hint" style="left:398px;top:561px">?</div>
  <div class="lbl" style="top:590px;width:207px">Photo</div>
  <div class="btn" style="left:223px;top:588px;width:83px">Browse</div>
  <div class="avatar" role="img" aria-label="Placeholder for the driver's profile photo"></div>
  <div class="hint" style="left:398px;top:604px">?</div>
  <div class="lbl" style="top:650px;width:212px">Signature</div>
  <div class="btn" style="left:223px;top:650px;width:83px">Browse</div>
  <div class="field" style="left:314px;top:649px;width:79px"></div>
  <div class="hint" style="left:398px;top:652px">?</div>
  <div class="lbl" style="top:680px;width:212px">Employee Code</div>
  <div class="field" style="left:224px;top:680px;width:169px">Doe</div>
  <div class="hint" style="left:398px;top:682px">?</div>

  <!-- personal: right column -->
  <div class="lbl" style="top:470px;width:696px">Street Address</div>
  <div class="field" style="left:714px;top:469px;width:169px">Doe</div>
  <div class="hint" style="left:889px;top:471px">?</div>
  <div class="lbl" style="top:500px;width:696px">Postcode</div>
  <div class="field" style="left:714px;top:499px;width:169px">Doe</div>
  <div class="hint" style="left:889px;top:501px">?</div>
  <div class="lbl" style="top:530px;width:696px">City</div>
  <div class="field" style="left:714px;top:529px;width:169px">Doe</div>
  <div class="hint" style="left:889px;top:531px">?</div>
  <div class="lbl" style="top:560px;width:696px">Country</div>
  <div class="field select" style="left:714px;top:559px;width:169px">Doe</div>
  <div class="hint" style="left:889px;top:561px">?</div>
  <div class="lbl" style="top:590px;width:696px">Phone Number</div>
  <div class="field" style="left:714px;top:589px;width:169px">Doe</div>
  <div class="hint" style="left:889px;top:591px">?</div>
  <div class="lbl" style="top:620px;width:696px">Email</div>
  <div class="field" style="left:714px;top:619px;width:169px">Doe</div>
  <div class="hint" style="left:889px;top:621px">?</div>
  <div class="lbl" style="top:650px;width:696px">Additional Information</div>
  <div class="field area" style="left:714px;top:649px;width:169px">Doe<br>Fill in</div>
  <div class="hint" style="left:889px;top:652px">?</div>
  <div class="lbl" style="top:694px;width:696px">Additional Restrictions</div>
  <div class="field area" style="left:714px;top:693px;width:169px">Doe<br>Fill in</div>
  <div class="hint" style="left:889px;top:696px">?</div>

  <div class="section-bar"></div>
  <div class="divider"></div>
  <div class="section-title" style="left:112px">Licence</div>
  <div class="section-title" style="left:554px">Certificate Status</div>

  <!-- licence -->
  <div class="lbl" style="top:808px;width:214px">Licence Number</div>
  <div class="field" style="left:225px;top:806px;width:116px">Doe</div>
  <div class="hint" style="left:348px;top:808px">?</div>
  <div class="lbl" style="top:838px;width:214px">Revoked</div>
  <div class="field select" style="left:225px;top:836px;width:116px">Doe</div>
  <div class="hint" style="left:348px;top:838px">?</div>
  <div class="lbl" style="top:868px;width:214px">Category</div>
  <div class="field select" style="left:225px;top:866px;width:116px">Doe</div>
  <div class="hint" style="left:348px;top:868px">?</div>
  <div class="lbl" style="top:898px;width:214px">Material</div>
  <div class="field select" style="left:225px;top:896px;width:116px">Doe</div>
  <div class="field select" style="left:349px;top:896px;width:56px">1977</div>
  <div class="field select" style="left:409px;top:896px;width:46px">Nov</div>
  <div class="field select" style="left:459px;top:896px;width:39px">24</div>
  <div class="hint" style="left:504px;top:898px">?</div>
  <div class="lbl" style="top:928px;width:214px">Infrastructure</div>
  <div class="field select" style="left:225px;top:926px;width:116px">Doe</div>
  <div class="field select" style="left:349px;top:926px;width:56px">1977</div>
  <div class="field select" style="left:409px;top:926px;width:46px">Nov</div>
  <div class="field select" style="left:459px;top:926px;width:39px">24</div>
  <div class="hint" style="left:504px;top:928px">?</div>

  <div class="group" style="left:113px;top:966px;width:318px;height:65px"></div>
  <div class="group-title" style="left:124px;top:973px">Language Competence</div>
  <div class="field select" style="left:124px;top:1001px;width:116px">Doe</div>
  <div class="field select" style="left:248px;top:1001px;width:55px">1977</div>
  <div class="field select" style="left:308px;top:1001px;width:46px">Nov</div>
  <div class="field select" style="left:358px;top:1001px;width:39px">24</div>
  <div class="hint" style="left:405px;top:1003px">?</div>

  <!-- certificate status -->
  <div class="lbl" style="top:808px;width:767px">Creation Date</div>
  <div class="field select" style="left:780px;top:806px;width:56px">1977</div>
  <div class="field select" style="left:840px;top:806px;width:46px">Nov</div>
  <div class="field select" style="left:890px;top:806px;width:39px">24</div>
  <div class="hint" style="left:938px;top:808px">?</div>
  <div class="lbl" style="top:838px;width:767px">Formal Expiry Date</div>
  <div class="field select" style="left:780px;top:836px;width:56px">1977</div>
  <div class="field select" style="left:840px;top:836px;width:46px">Nov</div>
  <div class="field select" style="left:890px;top:836px;width:39px">24</div>
  <div class="lbl" style="top:868px;width:767px">Reason for Suspension</div>
  <div class="field area" style="left:780px;top:866px;width:149px">Doe<br>Fill in</div>
  <div class="lbl" style="top:912px;width:767px">Date for Suspension</div>
  <div class="field select" style="left:780px;top:910px;width:56px">1977</div>
  <div class="field select" style="left:840px;top:910px;width:46px">Nov</div>
  <div class="field select" style="left:890px;top:910px;width:39px">24</div>
  <div class="hint" style="left:938px;top:912px">?</div>
  <div class="lbl" style="top:942px;width:767px">Reason for temporary suspension</div>
  <div class="field area" style="left:780px;top:940px;width:149px">Doe<br>Fill in</div>
  <div class="hint" style="left:938px;top:943px">?</div>
  <div class="lbl" style="top:986px;width:767px">Period for temporary suspension</div>
  <div class="field select" style="left:780px;top:984px;width:56px">1977</div>
  <div class="field select" style="left:840px;top:984px;width:46px">Nov</div>
  <div class="field select" style="left:890px;top:984px;width:39px">24</div>
  <div class="field select" style="left:948px;top:984px;width:56px">1977</div>
  <div class="field select" style="left:1008px;top:984px;width:46px">Nov</div>
  <div class="field select" style="left:1058px;top:984px;width:39px">24</div>
  <div class="lbl" style="top:1017px;width:767px">Report</div>
  <div class="field select" style="left:780px;top:1015px;width:149px">Doe</div>
  <div class="lbl" style="top:1047px;width:767px">Date Reported Destroyed</div>
  <div class="field select" style="left:780px;top:1046px;width:56px">1977</div>
  <div class="field select" style="left:840px;top:1046px;width:46px">Nov</div>
  <div class="field select" style="left:890px;top:1046px;width:39px">24</div>
  <div class="hint" style="left:938px;top:1048px">?</div>
  <div class="lbl" style="top:1077px;width:767px">Date of copy</div>
  <div class="field select" style="left:780px;top:1076px;width:56px">1977</div>
  <div class="field select" style="left:840px;top:1076px;width:46px">Nov</div>
  <div class="field select" style="left:890px;top:1076px;width:39px">24</div>
  <div class="hint" style="left:938px;top:1078px">?</div>

  <footer class="footer">
    <div class="left">Copyright © 2012 RailLedger. All Rights Reserved | Terms &amp; Conditions</div>
    <div class="right">Home | How it works | Pricing | Customers | About us | Contact</div>
  </footer>
</div>
</body>
</html>
```